Tallowmere Capital Partners- Business Card

We need a professional business card that conveys confidence and trust. Strength. A modern and still yet, traditional financial planner/advisor format. I will upload a logo file or two, you do not have to use it, if it does not work for the design.

Target Market(s)

high net worth

Industry/Entity Type

Finance

Contact Information for Business Card

Address: 24836 Orchard Ave. Suite 400, Huntington Beach, CA 93518, website: tallowmerecap.example, ph # (555) 271-6094, email address: rpoulsen@tallowmerecap.example

```html
<!DOCTYPE html>
<html lang="en">
<head>
<meta charset="utf-8">
<title>Tallowmere Capital Partners – Business Card</title>
<link rel="stylesheet" href="https://fonts.googleapis.com/css2?family=Playfair+Display:wght@500&family=Montserrat:wght@600&family=Roboto:wght@400&display=swap">
<style>
  :root {
    --stage: #2b2b2b;
    --stage-edge: #161616;
    --gold: #b8963f;
    --gold-soft: #c9a95a;
    --ink: #555555;
    --ink-light: #777777;
    --paper: #ffffff;
    --night: #111111;
    --night-soft: #1e1e1e;
    --rule: #cfcfcf;
  }
  * { box-sizing: border-box; margin: 0; padding: 0; }
  html, body { width: 1200px; height: 900px; overflow: hidden; }
  body {
    background: radial-gradient(ellipse at 55% 40%, var(--stage) 0%, var(--stage-edge) 100%);
    position: relative;
    font-family: "Roboto", Arial, sans-serif;
  }

  /* Back of card (portrait) */
  .card-back {
    position: absolute;
    left: 130px; top: 160px;
    width: 340px; height: 595px;
    border-radius: 22px;
    background: var(--night);
    border: 2px solid var(--gold);
    overflow: hidden;
    display: flex; align-items: center; justify-content: center;
  }
  .card-back__pattern {
    position: absolute; inset: 0;
    background: radial-gradient(ellipse at 50% 45%, var(--night-soft) 0%, var(--night) 75%);
  }
  .card-back__brand {
    position: relative;
    display: flex; align-items: center; gap: 10px;
    font-family: "Playfair Display", Georgia, serif;
    font-weight: 500;
    font-size: 15px;
    letter-spacing: 1px;
    color: var(--gold-soft);
    text-transform: uppercase;
    white-space: nowrap;
  }
  .card-back__brand .mark {
    width: 16px; height: 16px; border: 1.5px solid var(--gold-soft);
  }

  /* Front of card (landscape) */
  .card-front {
    position: absolute;
    left: 540px; top: 160px;
    width: 560px; height: 320px;
    border-radius: 22px;
    background: var(--paper);
    border: 2px solid var(--gold);
  }
  .brand {
    position: absolute; left: 40px; top: 40px;
    display: flex; align-items: center; gap: 12px;
    font-family: "Playfair Display", Georgia, serif;
    font-weight: 500;
    font-size: 21px;
    letter-spacing: 0.5px;
    color: var(--gold);
    text-transform: uppercase;
    white-space: nowrap;
  }
  .brand .mark {
    width: 22px; height: 22px; border: 2px solid var(--gold);
  }
  .person {
    position: absolute; right: 290px; top: 138px;
    text-align: right;
  }
  .person__name {
    font-family: "Montserrat", Arial, sans-serif;
    font-weight: 600;
    font-size: 17px;
    color: var(--gold);
    letter-spacing: 0.3px;
    white-space: nowrap;
  }
  .person__title {
    margin-top: 6px;
    font-size: 14px;
    color: var(--ink);
  }
  .divider {
    position: absolute; left: 285px; top: 128px;
    width: 1px; height: 130px;
    background: var(--rule);
  }
  .contact {
    position: absolute; left: 304px; top: 132px;
    font-size: 13.5px;
    color: var(--ink);
    line-height: 1.45;
  }
  .contact__address { margin-bottom: 8px; }
  .contact__list { list-style: none; }
  .contact__list li {
    display: flex; align-items: center; gap: 8px;
    white-space: nowrap;
  }
  .contact__list svg { width: 12px; height: 12px; flex: none; }
</style>
</head>
<body>

  <section class="card-back">
    <div class="card-back__pattern" role="img" aria-label="Repeating embossed pattern of the company emblem on black"></div>
    <div class="card-back__brand"><span class="mark"></span>Tallowmere Capital Partners</div>
  </section>

  <section class="card-front">
    <div class="brand"><span class="mark"></span>Tallowmere Capital Partners</div>

    <div class="person">
      <p class="person__name">RENATA J. POULSEN</p>
      <p class="person__title">Founder &amp; CEO</p>
    </div>

    <div class="divider"></div>

    <div class="contact">
      <p class="contact__address">24836 Orchard Ave.<br>Suite 400 Huntington Beach, CA 93518</p>
      <ul class="contact__list">
        <li>
          <svg viewBox="0 0 12 12"><rect width="12" height="12" rx="2" fill="#b8963f"/><path d="M3.5 3c.6-.4 1.1 0 1.4.7.2.5-.2.8-.4 1 .3.9.9 1.5 1.8 1.8.2-.2.5-.6 1-.4.7.3 1.1.8.7 1.4-.6.9-2 .7-3.5-.8S2.6 3.6 3.5 3z" fill="#fff"/></svg>
          555 271 6094
        </li>
        <li>
          <svg viewBox="0 0 12 12"><rect y="2" width="12" height="8" rx="1" fill="#b8963f"/><path d="M1 3l5 3.5L11 3" stroke="#fff" stroke-width="1" fill="none"/></svg>
          info@tallowmerecap.example
        </li>
        <li>
          <svg viewBox="0 0 12 12"><circle cx="6" cy="6" r="6" fill="#b8963f"/><path d="M6 2.5c1.4 0 2.3 1 2.3 2.2C8.3 6.3 6 9.5 6 9.5S3.7 6.3 3.7 4.7C3.7 3.5 4.6 2.5 6 2.5z" fill="#fff"/></svg>
          www.tallowmerecap.example
        </li>
      </ul>
    </div>
  </section>

</body>
</html>
```